Business card for plumber

I need a business card for my plumbing company.
on it should:
Surname
position
E-mail
Telephone & mobile phone
Website
Please everything as placeholders / fantasy names.
We stand for high quality, hygiene and professionalism.

Colours:
# 606060 anthracite
# f7931e orange
# 2b89cc blue

Industry/Entity Type

Plumber

Contact Information for Business Card

folgt...

```html
<!DOCTYPE html>
<html lang="en">
<head>
<meta charset="utf-8">
<title>Aldwin Haustechnik – Business Card</title>
<link href="https://fonts.googleapis.com/css2?family=Arimo:wght@400;700&display=swap" rel="stylesheet">
<style>
  :root {
    --stage: #2b2b2b;
    --card: #1b1b1c;
    --blue: #2b89cc;
    --orange: #f7931e;
    --white: #ffffff;
    --anthracite: #606060;
  }
  * { box-sizing: border-box; margin: 0; padding: 0; }
  html, body { width: 1200px; height: 988px; overflow: hidden; }
  body {
    background: var(--stage);
    font-family: "Arimo", Arial, sans-serif;
    position: relative;
  }
  .card {
    position: absolute;
    left: 280px;
    width: 640px;
    height: 366px;
    background: var(--card);
    border-radius: 20px;
    box-shadow: 0 10px 30px rgba(0,0,0,.45);
    overflow: hidden;
  }
  .card--front { top: 70px; }
  .card--back { top: 552px; }

  /* front */
  .brand {
    position: absolute;
    inset: 0;
    display: flex;
    align-items: center;
    justify-content: center;
    gap: 18px;
  }
  .brand__mark {
    width: 54px; height: 54px;
    border-radius: 50%;
    background: var(--orange);
  }
  .brand__name {
    color: var(--blue);
    font-weight: 700;
    font-size: 38px;
    line-height: 1.05;
    letter-spacing: .5px;
    text-transform: uppercase;
  }

  /* back */
  .accent-bar {
    position: absolute;
    left: 0; top: 108px;
    width: 12px; height: 40px;
    background: var(--blue);
  }
  .person {
    position: absolute;
    left: 44px; top: 100px;
  }
  .person__name {
    font-weight: 700;
    font-size: 27px;
    letter-spacing: .3px;
    text-transform: uppercase;
  }
  .person__first { color: var(--blue); }
  .person__last { color: var(--orange); }
  .person__role {
    color: var(--white);
    font-size: 15px;
    margin-top: 3px;
  }
  .address {
    position: absolute;
    left: 44px; top: 178px;
    color: var(--white);
    font-size: 15px;
    line-height: 1.3;
  }
  .contacts {
    position: absolute;
    left: 44px; top: 240px;
    list-style: none;
    color: var(--white);
    font-size: 15px;
    line-height: 1.45;
  }
  .contacts li { display: flex; align-items: center; gap: 8px; }
  .contacts svg { width: 13px; height: 13px; fill: var(--orange); flex: none; }

  .brand--back {
    left: auto; right: 36px; top: 40px; bottom: auto;
    inset: auto;
    position: absolute;
    right: 40px; top: 56px;
    flex-direction: column;
    align-items: center;
    gap: 14px;
  }
  .brand--back .brand__mark { width: 150px; height: 150px; }
  .brand--back .brand__name { font-size: 22px; text-align: center; }
</style>
</head>
<body>

<section class="card card--front" aria-label="Card front">
  <div class="brand">
    <span class="brand__mark" aria-hidden="true"></span>
    <span class="brand__name">Aldwin<br>Haustechnik</span>
  </div>
</section>

<section class="card card--back" aria-label="Card back">
  <span class="accent-bar" aria-hidden="true"></span>
  <div class="person">
    <p class="person__name"><span class="person__first">Jonas</span> <span class="person__last">Berger</span></p>
    <p class="person__role">Managing Director</p>
  </div>
  <p class="address">48 Linden Way, 2nd Floor CD<br>Road Northfield - Country</p>
  <ul class="contacts">
    <li><svg viewBox="0 0 16 16" aria-hidden="true"><path d="M3 1l3 3-2 2c1 2 3 4 5 5l2-2 3 3-2 3C6 15 1 10 0 3z"/></svg>(555)201-3380</li>
    <li><svg viewBox="0 0 16 16" aria-hidden="true"><path d="M4 0h8v16H4zM5.5 2v10h5V2z"/></svg>(555)201-3381</li>
    <li><svg viewBox="0 0 16 16" aria-hidden="true"><path d="M0 3h16v10H0zM1.5 4.5L8 9l6.5-4.5z"/></svg>info@aldwinhaustechnik.com</li>
    <li><svg viewBox="0 0 16 16" aria-hidden="true"><circle cx="8" cy="8" r="7.5"/></svg>www.aldwinhaustechnik.com</li>
  </ul>
  <div class="brand brand--back">
    <span class="brand__mark" aria-hidden="true"></span>
    <span class="brand__name">Aldwin<br>Haustechnik</span>
  </div>
</section>

</body>
</html>
```